Business Card Design - R.T. Custom Cabinets Ltd.

Design a business card, including a new logo for a new company in Vancouver, British Columbia, Canada.

The logo must be available as a separate file.

The card should include all company information including:
R.T. Custom Cabinets Ltd.
2786 Larchmoor Crescent
Burnaby, B.C. V7K 2P9
Telehone: 604-XXX-XXXX
Fax: 604-XXX-XXXX
www.rtcustomcabinets.example

As well as individual contact information for employees:
Name
Position
Telephone
Email

The card must include a thoughtful message as well

Target Market(s)

Custom Cabinets

Industry/Entity Type

Business

Contact Information for Business Card

Important information on the front, thoughtful message on the back

Colors
fbed22
9bcb3c
0355a3
ec1f27

Requirements
Must have
• See project description
Nice to have
• images that showcase custom cabinets (european, modern and traditional) styles

```html
<!DOCTYPE html>
<html lang="en">
<head>
<meta charset="utf-8">
<title>R.T. Custom Cabinets Ltd. – Business Card</title>
<link href="https://fonts.googleapis.com/css2?family=Source+Sans+3:wght@400;600;700&family=Kumbh+Sans:wght@600&display=swap" rel="stylesheet">
<style>
  :root {
    --brand-red: #ec1f27;
    --brand-yellow: #fbed22;
    --brand-green: #9bcb3c;
    --brand-blue: #0355a3;
    --paper: #ffffff;
    --ink: #2b2b2b;
    --backdrop: #ecebea;
  }
  * { margin: 0; padding: 0; box-sizing: border-box; }
  html, body { width: 1200px; height: 900px; overflow: hidden; }
  body {
    position: relative;
    background: var(--backdrop);
    font-family: "Source Sans 3", "Myriad Pro", sans-serif;
  }
  .card {
    position: absolute;
    background: var(--paper);
    overflow: hidden;
    box-shadow: 0 4px 14px rgba(0,0,0,0.12);
  }

  /* Front card */
  .card-front { left: 78px; top: 34px; width: 588px; height: 364px; }
  .contact-panel {
    position: absolute; left: 0; top: 49px; width: 326px; height: 268px;
    background: var(--brand-red); color: var(--paper);
    padding: 9px 0 0 31px;
  }
  .person-name { font-size: 22px; font-weight: 700; line-height: 27px; }
  .person-title { font-size: 15.5px; line-height: 18px; }
  .company-name { font-size: 16px; font-weight: 700; margin-top: 17px; line-height: 24px; }
  .address-line { font-size: 16px; line-height: 24.5px; }
  .contact-list { list-style: none; margin-top: 15px; }
  .contact-list li { display: flex; align-items: center; font-size: 16px; line-height: 24.5px; }
  .contact-list svg { width: 12px; height: 12px; margin-right: 7px; fill: var(--paper); flex: none; }
  .logo-frame {
    position: absolute; left: 347px; top: 88px; width: 200px; height: 200px;
    border: 6px solid var(--brand-red);
  }
  .logo-frame .mark {
    position: absolute; left: 44px; top: 44px; width: 100px; height: 100px;
    background: var(--brand-red);
  }
  .edge-strip {
    position: absolute; left: 568px; top: 49px; width: 20px; height: 268px;
    background: var(--brand-red);
  }
  .accent-bar {
    position: absolute; left: 347px; top: 300px; width: 200px; height: 5px;
    display: flex;
  }
  .accent-bar span { flex: 1; }
  .accent-yellow { background: var(--brand-yellow); }
  .accent-green { background: var(--brand-green); }
  .accent-blue { background: var(--brand-blue); }

  /* Back card */
  .card-back { left: 388px; top: 505px; width: 567px; height: 352px; }
  .band { position: absolute; left: 0; width: 100%; background: var(--brand-red); }
  .band-top { top: 0; height: 110px; }
  .band-bottom {
    top: 241px; height: 111px;
    display: flex; align-items: center; justify-content: center;
  }
  .accent-stripes {
    position: absolute; left: 0; width: 100%; height: 4px; display: flex;
  }
  .accent-stripes span { flex: 1; }
  .stripes-top { top: 110px; }
  .stripes-bottom { top: 237px; }
  .brand-row {
    position: absolute; left: 52px; top: 145px;
    display: flex; align-items: center; gap: 21px;
  }
  .brand-square {
    width: 61px; height: 61px; border: 2px solid var(--brand-red);
  }
  .brand-name {
    font-family: "Kumbh Sans", "Century Gothic", sans-serif;
    font-weight: 600;
    font-size: 29px; color: var(--ink); letter-spacing: 0.2px;
    margin-top: 10px;
  }
  .card-message {
    font-size: 19px; font-weight: 600; color: var(--paper);
    letter-spacing: 0.3px; text-align: center;
  }
</style>
</head>
<body>

<section class="card card-front" aria-label="Business card front">
  <div class="contact-panel">
    <p class="person-name">Daniel Hartley</p>
    <p class="person-title">Managing Director</p>
    <p class="company-name">R.T. Custom Cabinets Ltd.</p>
    <p class="address-line">2786 Larchmoor Crescent</p>
    <p class="address-line">Burnaby, B.C. V7K 2P9</p>
    <ul class="contact-list">
      <li><svg viewBox="0 0 24 24" aria-hidden="true"><path d="M6.6 10.8a15.1 15.1 0 0 0 6.6 6.6l2.2-2.2c.3-.3.7-.4 1-.2 1.1.4 2.3.6 3.6.6.6 0 1 .4 1 1V20c0 .6-.4 1-1 1A17 17 0 0 1 3 4c0-.6.4-1 1-1h3.5c.6 0 1 .4 1 1 0 1.3.2 2.5.6 3.6.1.3 0 .7-.2 1z"/></svg>604-XXX-XXXX</li>
      <li><svg viewBox="0 0 24 24" aria-hidden="true"><path d="M6 2h9l3 3v5h2a2 2 0 0 1 2 2v8a2 2 0 0 1-2 2H4a2 2 0 0 1-2-2v-8a2 2 0 0 1 2-2h2zm2 2v6h8V6h-2V4zm-2 10v2h3v-2zm5 0v2h3v-2zm5 0v2h3v-2zm-10 3v2h3v-2zm5 0v2h3v-2zm5 0v2h3v-2z"/></svg>604-XXX-XXXX</li>
      <li><svg viewBox="0 0 24 24" aria-hidden="true"><path d="M2 5h20v14H2zm2 2v.5l8 5 8-5V7l-8 5z"/></svg>info@rtcustomcabinets.example</li>
      <li><svg viewBox="0 0 24 24" aria-hidden="true"><path d="M12 2a10 10 0 1 0 0 20 10 10 0 0 0 0-20zm-1 17.9A8 8 0 0 1 4.2 10L9 14.8v1a2 2 0 0 0 2 2zm6.9-2.5A2 2 0 0 0 16 16h-1v-3a1 1 0 0 0-1-1H8v-2h2a1 1 0 0 0 1-1V7h2a2 2 0 0 0 2-2v-.4a8 8 0 0 1 2.9 12.8z"/></svg>www.rtcustomcabinets.example</li>
    </ul>
  </div>
  <div class="logo-frame"><span class="mark"></span></div>
  <div class="accent-bar" aria-hidden="true">
    <span class="accent-yellow"></span><span class="accent-green"></span><span class="accent-blue"></span>
  </div>
  <div class="edge-strip"></div>
</section>

<section class="card card-back" aria-label="Business card back">
  <div class="band band-top"></div>
  <div class="accent-stripes stripes-top" aria-hidden="true">
    <span class="accent-yellow"></span><span class="accent-green"></span><span class="accent-blue"></span>
  </div>
  <div class="brand-row">
    <span class="brand-square"></span>
    <span class="brand-name">R.T Custom Cabinets Ltd.</span>
  </div>
  <div class="accent-stripes stripes-bottom" aria-hidden="true">
    <span class="accent-blue"></span><span class="accent-green"></span><span class="accent-yellow"></span>
  </div>
  <div class="band band-bottom">
    <p class="card-message">Crafted with care for the heart of your home.</p>
  </div>
</section>

</body>
</html>
```